stationary for home builder
Birchwood Custom Homes, Inc.
Project: stationary for home builder
stationary for home builder - Real Estate
Creative Brief
Professional
Dale Morrow
President
4200 Tern Avenue, suite 310 Cedar Cove, CA 90210
bchdalemorrow@mailvista.test

```html
<!DOCTYPE html>
<html lang="en">
<head>
<meta charset="utf-8">
<title>Birchwood Custom Homes, Inc. — Business Cards</title>
<link rel="stylesheet" href="https://fonts.googleapis.com/css2?family=Cinzel:wght@400;600&family=Cormorant+Garamond:wght@500&display=swap">
<style>
  :root {
    --stage: #6f7275;
    --brand-red: #c8161d;
    --brand-red-dark: #8c0d12;
    --brand-red-light: #e0262c;
    --silver: #b9bbbe;
    --silver-dark: #8d9094;
    --paper: #ffffff;
    --ink: #4a4c4f;
    --serif: "Cinzel", serif;
    --body: "Cormorant Garamond", serif;
  }
  * { margin: 0; padding: 0; box-sizing: border-box; }
  html, body { width: 1200px; height: 908px; overflow: hidden; }
  body {
    background: var(--stage);
    display: flex;
    align-items: center;
    justify-content: center;
    gap: 40px;
  }
  .card {
    position: relative;
    width: 540px;
    height: 310px;
    border-radius: 18px;
    overflow: hidden;
  }
  .card--front {
    background: linear-gradient(135deg, var(--brand-red-light) 0%, var(--brand-red) 45%, var(--brand-red-dark) 100%);
  }
  .card--front .company-name {
    position: absolute;
    right: 36px;
    top: 128px;
    display: flex;
    align-items: center;
    gap: 10px;
    font-family: var(--serif);
    font-weight: 400;
    font-size: 20px;
    letter-spacing: 1px;
    color: var(--paper);
  }
  .mark-square { width: 14px; height: 14px; background: currentColor; flex: none; }
  .card--back { background: var(--paper); }
  .card--back .swoosh { position: absolute; inset: 0; }
  .card--back .company-name {
    position: absolute;
    left: 28px;
    top: 140px;
    display: flex;
    align-items: center;
    gap: 8px;
    font-family: var(--serif);
    font-weight: 400;
    font-size: 15px;
    letter-spacing: 0.5px;
    color: var(--brand-red);
  }
  .person {
    position: absolute;
    right: 180px;
    top: 40px;
    text-align: right;
    font-family: var(--serif);
  }
  .person__name { font-size: 15px; font-weight: 600; color: var(--brand-red); letter-spacing: 0.5px; }
  .person__title { font-size: 11px; color: var(--ink); letter-spacing: 1px; }
  .contact {
    position: absolute;
    right: 180px;
    top: 190px;
    text-align: right;
    font-family: var(--body);
    font-size: 12px;
    line-height: 1.45;
    color: var(--ink);
  }
</style>
</head>
<body>
  <section class="card card--front" aria-label="Card front">
    <div class="company-name"><span class="mark-square"></span>BIRCHWOOD CUSTOM HOMES, INC.</div>
  </section>

  <section class="card card--back" aria-label="Card back">
    <svg class="swoosh" width="540" height="310" viewBox="0 0 540 310" aria-hidden="true">
      <defs>
        <linearGradient id="redBand" x1="0" y1="0" x2="1" y2="1">
          <stop offset="0" stop-color="var(--brand-red-light)"/>
          <stop offset="1" stop-color="var(--brand-red-dark)"/>
        </linearGradient>
        <linearGradient id="silverBand" x1="0" y1="0" x2="1" y2="0">
          <stop offset="0" stop-color="var(--silver)"/>
          <stop offset="1" stop-color="var(--silver-dark)"/>
        </linearGradient>
      </defs>
      <path d="M360 0 C300 90 470 200 380 310 L540 310 L540 0 Z" fill="url(#silverBand)"/>
      <path d="M395 0 C340 90 500 200 415 310 L540 310 L540 0 Z" fill="var(--paper)"/>
      <path d="M410 0 C360 90 515 200 430 310 L540 310 L540 0 Z" fill="url(#redBand)"/>
    </svg>
    <div class="company-name"><span class="mark-square"></span>BIRCHWOOD CUSTOM HOMES, INC.</div>
    <div class="person">
      <div class="person__name">DALE MORROW</div>
      <div class="person__title">PRESIDENT</div>
    </div>
    <div class="contact">
      4200 Tern Avenue, suite 310<br>
      Cedar Cove, CA 90210<br>
      949 555 0142<br>
      949 555 0187<br>
      bchdalemorrow@mailvista.test
    </div>
  </section>
</body>
</html>
```